Brisk Treadway - Design Australia's largest Tyre ecommerce website!

We need a home page design and headers for the other pages.

Our site is built on magento community and is up and running at
brisktreadway.com.au
so you can see what we do. Basically all the elements on the current home page are required but don't have to stay in the current form. This is just a template we used to get the site functional with little regard to design.

We are the only tyre company in Australia that is 100% online. We sell tyres for almost every vehicle including motor bikes, cars, 4x4, trucks tractors, ATVs mining equipment. We have no shopfront, we dont fit tyres or run a shopfront. We just sell and ship tyres at the best prices possible.

We want a design that
* uses complimentary colours to our logo.
* has space for the video and tyre chooser - without scrolling the tyre chooser needs to be visible at least in part. The chooser is a key element. This is how most customers will find their tyre.
* in the header or somewhere prominent on the homepage we want to advertise
Australia Wide Delivery
Free delivery to Brisbane Sydney Melbourne
$20 to all other locations **with few exceptions (the small print)
Fast Delivery to your door -
1-3 Business days to most metro areas
5-10 Business days to all other areas **With few exceptions

On the home page we also want
* links to our facebook and twitter accounts
* a specials banner/space, with space to display up to 20 items.
* customer testimonials space

Thanks in advance!
Updates

Hi - It is in the job description but just to emphasise, the tyre chooser and intro video are key elements of our page and we need users to be drawn to them in a very visual way. Not flashing neon lights but some kind of elegant clean design. 

There are two paths a user may take - most will go straight to the tyre chooser to find their product. The rest will click on a category and then use the "shop by" filters to quickly refine their search.

Target Market(s)

18-30 Male retail. Truck and heavy equipment companies

Industry/Entity Type

Business

Requirements
Must have
• We want a design that
Australia Wide Delivery
Nice to have
• Possibly a graphic that indicates that we sell all tyres and not just cars and 4x4

```html
<!DOCTYPE html>
<html lang="en">
<head>
<meta charset="utf-8">
<title>Brisk Treadway – Your Online Tyre Company</title>
<link href="https://fonts.googleapis.com/css2?family=Roboto:wght@300;400;500;700&family=Titillium+Web:wght@400;600&display=swap" rel="stylesheet">
<style>
:root{
  --black:#000;
  --nav:#2e2e2e;
  --red:#c8090d;
  --red-dark:#9c0508;
  --blue:#1565b8;
  --blue-deep:#123f86;
  --cyan:#19a3d8;
  --text:#777;
  --dark:#222;
  --line:#d8d8d8;
  --footer:#2b2b2b;
  --footer-base:#222;
}
*{margin:0;padding:0;box-sizing:border-box}
html,body{width:935px;height:1200px;overflow:hidden;background:#fff}
body{position:relative;font-family:"Roboto",sans-serif;color:var(--dark)}
.abs{position:absolute}
a{color:inherit;text-decoration:none}

/* header */
.site-header{left:0;top:0;width:935px;height:93px;background:var(--black)}
.brand{left:94px;top:30px;color:#fff;font-weight:700;font-size:24px;letter-spacing:.5px;line-height:1}
.brand small{display:block;font-size:8px;font-weight:700;letter-spacing:1px;margin-top:5px;color:#fff}
.brand .dot{display:inline-block;width:12px;height:12px;background:var(--red);margin-right:7px;vertical-align:2px}
.social{left:770px;top:14px;display:flex;gap:7px}
.social span{width:13px;height:13px;border-radius:50%;background:#6a6a6a}
.account-links{left:421px;top:46px;display:flex;gap:16px;font-size:10px;color:#fff}
.search{left:659px;top:39px;width:183px;height:28px;background:#444;color:#ccc;font-size:9px;padding:9px 8px}
.search svg{position:absolute;right:8px;top:9px}

/* nav */
.main-nav{left:0;top:93px;width:935px;height:39px;background:var(--nav)}
.main-nav ul{list-style:none;font-size:11.5px;color:#fff;font-weight:500}
.main-nav li{position:absolute;top:12px;white-space:nowrap}
.cart{left:710px;top:93px;width:133px;height:39px;background:var(--red);color:#fff;font-size:10px;display:flex;align-items:center;padding-left:14px;gap:12px}

/* hero */
.hero{left:0;top:132px;width:935px;height:251px;background:linear-gradient(100deg,#2d2d2b 0%,#4b4f47 35%,#6f7568 55%,#3a3a37 75%,#1a1a1a 100%)}
.hero h1{position:absolute;left:105px;top:48px;color:#fff;font-weight:300;font-size:36px;line-height:42px}
.hero h1 b{font-weight:700}
.btn{background:var(--red);color:#fff;font-size:11px;font-weight:500;display:flex;align-items:center;justify-content:center}
.hero .btn{position:absolute;left:105px;top:141px;width:66px;height:25px}

/* panels */
.panel-head{background:var(--blue);color:#fff;font-family:"Titillium Web",sans-serif;padding:5px 15px 0}
.panel-head h2{font-weight:400;font-size:20px;line-height:22px}
.panel-head p{font-size:13px;line-height:20px}
.video{left:94px;top:414px;width:286px;height:251px}
.video .panel-head{height:51px}
.video-frame{height:200px;background:linear-gradient(180deg,#9c9c98,#5a5a58 60%,#7d7d7a);position:relative}
.video-frame svg{position:absolute;left:128px;top:85px}

.chooser{left:398px;top:414px;width:447px;height:251px;border:1px solid var(--line);border-top:none}
.chooser .panel-head{height:51px;margin:0 -1px}
.tabs{position:absolute;left:11px;top:60px;display:flex;font-size:10px;color:#555}
.tabs span{height:25px;border:1px solid #ccc;display:flex;align-items:center;padding:0 18px;background:#fff}
.tabs span.on{background:#efefef}
.tyre-size{position:absolute;left:-1px;top:95px;width:135px;height:104px;background:linear-gradient(135deg,#4a4a4a,#9a9a9a 60%,#d4d4d4)}
.field{position:absolute;width:117px;height:24px;background:#eef1f4;border:1px solid #dde2e6;font-size:10px;color:#666;padding:5px 9px}
.field::after{content:"";position:absolute;right:0;top:0;border-top:11px solid var(--cyan);border-left:11px solid transparent}
.chooser-note{position:absolute;left:7px;top:212px;font-size:8.5px;line-height:14px;color:#999;width:270px}
.chooser .btn{position:absolute;left:320px;top:213px;width:108px;height:28px;font-size:11px;background:linear-gradient(var(--red),var(--red-dark))}

/* welcome */
.welcome{left:94px;top:693px;width:285px}
.welcome h2{font-family:"Titillium Web",sans-serif;font-weight:400;font-size:20px;color:#111;line-height:24px}
.welcome p{font-size:10px;line-height:17px;color:#999;margin-top:2px}
.welcome .btn{width:65px;height:25px;margin-top:18px}

.delivery{left:391px;top:694px;width:451px;height:119px;background:radial-gradient(ellipse at 80% 45%,#2a6cc2,var(--blue-deep) 70%);color:#fff;box-shadow:0 5px 4px -3px rgba(0,0,0,.35)}
.delivery h3{position:absolute;left:12px;top:5px;font-size:17px;font-weight:700;line-height:24px}
.delivery .rate{position:absolute;left:12px;top:55px;font-size:14px}
.delivery .fine{position:absolute;left:12px;top:79px;font-size:8.5px;line-height:14px}
.delivery svg{position:absolute;left:315px;top:14px}
.delivery .tag{position:absolute;left:280px;top:85px;font-size:13px;font-weight:700}

/* brands */
.brands-rule{left:94px;width:748px;height:1px;background:var(--line)}
.brands{left:84px;top:870px;width:770px;height:36px;display:flex;align-items:center;justify-content:space-between;color:#bbb;font-size:14px}
.brand-mark{font-weight:700;font-size:13px;color:#333;width:90px;text-align:center}

/* footer */
.site-footer{left:0;top:950px;width:935px;height:208px;background:var(--footer)}
.col{position:absolute;top:18px;color:#fff}
.col h4{font-size:13px;font-weight:500;padding-bottom:6px;border-bottom:1px solid #555;width:108px}
.col ul{list-style:none;margin-top:8px;font-size:10px;line-height:17.5px;padding-left:2px;color:#eee}
.footer-base{left:0;top:1158px;width:935px;height:42px;background:var(--footer-base);color:#eee;font-size:10px;padding:21px 94px}
</style>
</head>
<body>

<header class="abs site-header">
  <div class="abs brand"><span class="dot"></span>BRISK TREADWAY<small>YOUR ONLINE TYRE COMPANY</small></div>
  <div class="abs social" aria-label="Social links"><span></span><span></span><span></span><span></span></div>
  <nav class="abs account-links"><a>My Account</a><a>My Wishlist</a><a>Checkout</a><a>Log in</a></nav>
  <div class="abs search">Search...
    <svg width="10" height="10" viewBox="0 0 10 10"><circle cx="4" cy="4" r="3" fill="none" stroke="#fff" stroke-width="1.4"/><line x1="6.2" y1="6.2" x2="9.5" y2="9.5" stroke="#fff" stroke-width="1.6"/></svg>
  </div>
</header>

<nav class="abs main-nav">
  <ul>
    <li style="left:94px">Home</li>
    <li style="left:146px">Car</li>
    <li style="left:186px">4x4</li>
    <li style="left:226px">Light Truck</li>
    <li style="left:303px">Truck</li>
    <li style="left:353px">Agriculture/OTR</li>
    <li style="left:454px">Motorbike</li>
    <li style="left:526px">Trailer/Caravan</li>
    <li style="left:624px">Rims</li>
    <li style="left:670px">Tubes</li>
  </ul>
</nav>
<div class="abs cart">
  <svg width="16" height="14" viewBox="0 0 16 14"><path d="M0 1h3l2 8h9l2-6H4" fill="none" stroke="#fff" stroke-width="1.6"/><circle cx="6" cy="12" r="1.5" fill="#fff"/><circle cx="13" cy="12" r="1.5" fill="#fff"/></svg>
  View Cart - $0.00
</div>

<section class="abs hero" role="img" aria-label="Coastal road winding into the distance with a tyre close-up in the foreground">
  <h1><b>Lorem Ipsum</b> Dolor<br>Sit Amet <b>2013</b></h1>
  <a class="btn">Read More</a>
</section>

<section class="abs video">
  <div class="panel-head"><h2>SURF SAFELY!</h2><p>Lorem Ipsum est simplement du faux</p></div>
  <div class="video-frame" role="img" aria-label="Intro video still of a tyre warehouse with shelves of tyres">
    <svg width="30" height="34" viewBox="0 0 30 34"><path d="M2 2l26 15L2 32z" fill="#fff" fill-opacity=".85"/></svg>
  </div>
</section>

<section class="abs chooser">
  <div class="panel-head"><h2>TYRE CHOOSER</h2><p>Please select from the boxes to find your Tyres.</p></div>
  <div class="tabs"><span class="on">Metric</span><span>Standard</span></div>
  <div class="tyre-size" role="img" aria-label="Illustration of a wheel and tyre sidewall with the size marking highlighted"></div>
  <div class="field" style="left:180px;top:99px">Width</div>
  <div class="field" style="left:312px;top:99px">Profile or Height</div>
  <div class="field" style="left:180px;top:137px">Rim</div>
  <div class="field" style="left:312px;top:137px">Brand</div>
  <div class="field" style="left:180px;top:175px">Vehicle</div>
  <div class="field" style="left:312px;top:175px">Accessories</div>
  <p class="chooser-note">Lorem Ipsum est simplement du faux texte employé dans la sition et la misen page avant impression.</p>
  <a class="btn">FIND MY TYRES</a>
</section>

<section class="abs welcome">
  <h2>WELCOME TO OUR SITE</h2>
  <p>Sed ut perspiciatis unde omnis iste natus error sit voluptatem accusantium doloremque laudantium, totam rem aperiam, eaque ipsa quae ab illo inventore veritatis et quasi architecto beatae vitae dicta sunt explicabo.</p>
  <a class="btn">Read More</a>
</section>

<aside class="abs delivery">
  <h3>Free Delivery To<br>“Brisbane Sydney Melbourne”</h3>
  <p class="rate">$20 to all other locations</p>
  <p class="fine">Fast Delivery to your door 1-3 Business days to most metro<br>areas 5-10 Business days to all other areas</p>
  <svg width="90" height="58" viewBox="0 0 90 58"><rect x="0" y="10" width="24" height="34" rx="2" fill="#fff"/><rect x="5" y="16" width="12" height="10" fill="var(--blue-deep)"/><rect x="27" y="0" width="63" height="44" rx="2" fill="#fff"/><g fill="#fff" stroke="var(--blue-deep)" stroke-width="3"><circle cx="15" cy="46" r="9"/><circle cx="55" cy="46" r="9"/><circle cx="77" cy="46" r="9"/></g></svg>
  <p class="tag">Australia Wide Delivery</p>
</aside>

<div class="abs brands-rule" style="top:850px"></div>
<div class="abs brands">
  <span>‹</span>
  <span class="brand-mark">Velo Tyres</span>
  <span class="brand-mark">Hardwick Tires</span>
  <span class="brand-mark">Kestra Tires</span>
  <span class="brand-mark">Marlo</span>
  <span class="brand-mark">Nanwell</span>
  <span>›</span>
</div>
<div class="abs brands-rule" style="top:927px"></div>

<footer class="abs site-footer">
  <div class="col" style="left:94px"><h4>Information</h4><ul><li>About Us</li><li>Customer Services</li><li>Privacy Policy</li><li>Site Map</li><li>Search Terms</li><li>Advanced Search</li><li>Orders and Returns</li><li>Contact Us</li></ul></div>
  <div class="col" style="left:280px"><h4 style="width:132px">Why Buy From Us</h4><ul><li>Shipping &amp; Returns</li><li>Secure Shopping</li><li>Dolor Sit Amet</li><li>Consectetur</li><li>Adipisicing Elit</li></ul></div>
  <div class="col" style="left:489px"><h4 style="width:92px">My Account</h4><ul><li>Sign In</li><li>View Cart</li><li>My Wishlist</li></ul></div>
  <div class="col" style="left:660px"><h4 style="width:108px">Brisk Treadway</h4><ul><li>No Risk Guarantee</li><li>High Rollers</li><li>FAQ</li></ul></div>
</footer>
<div class="abs footer-base">Copyright © 2013 Brisk Treadway. All Rights Reserved.</div>

</body>
</html>
```